Brintell's Business Card

I need some designs for a new business card including the new logo attached. An old example of our business card is also attached to show all the data that should be included on the new design.
**I added some more examples someone had mocked up**

Contact Information for Business Card

Should include all info on other examples uploaded.

```html
<!DOCTYPE html>
<html lang="en">
<head>
<meta charset="utf-8">
<title>Brintell's Business Card</title>
<link rel="stylesheet" href="https://fonts.googleapis.com/css2?family=Montserrat:wght@700&family=Open+Sans:wght@400;600&display=swap">
<style>
  :root {
    --brand-blue: #0f73bb;
    --brand-red: #e8202b;
    --ink: #1a1a1a;
    --paper: #ffffff;
    --backdrop: #141414;
  }
  * { box-sizing: border-box; margin: 0; padding: 0; }
  html, body { width: 1200px; height: 960px; overflow: hidden; }
  body {
    background: radial-gradient(ellipse at center, #2a2a2a 0%, var(--backdrop) 70%);
    font-family: "Open Sans", Arial, sans-serif;
    position: relative;
  }
  .card {
    position: absolute;
    width: 722px;
    height: 413px;
    background: var(--paper);
    overflow: hidden;
  }
  .card--front { left: 132px; top: 71px; }
  .card--back { left: 294px; top: 513px; }

  .wordmark {
    font-family: "Montserrat", Arial, sans-serif;
    font-weight: 700;
    color: var(--brand-blue);
    display: flex;
    align-items: center;
    line-height: 1;
  }
  .wordmark__dot {
    background: var(--brand-red);
    border-radius: 50%;
    flex: none;
  }
  .card--front .wordmark {
    position: absolute;
    left: 38px;
    top: 64px;
    font-size: 40px;
    gap: 14px;
  }
  .card--front .wordmark__dot { width: 34px; height: 34px; }

  .accent-panel { position: absolute; inset: 0; }

  .contact { position: absolute; left: 38px; top: 282px; }
  .contact__name {
    font-weight: 600;
    font-size: 28px;
    color: var(--brand-blue);
    margin-bottom: 10px;
  }
  .contact__line {
    display: flex;
    align-items: center;
    gap: 12px;
    font-size: 18px;
    color: var(--ink);
    height: 30px;
  }
  .contact__icon { width: 18px; height: 18px; flex: none; }

  .credentials {
    position: absolute;
    left: 432px;
    top: 278px;
    color: var(--paper);
    font-size: 18px;
    line-height: 30px;
  }

  .card--back .wordmark {
    position: absolute;
    left: 0; right: 0;
    top: 166px;
    justify-content: center;
    font-size: 64px;
    gap: 20px;
  }
  .card--back .wordmark__dot { width: 54px; height: 54px; }

  .service-area {
    position: absolute;
    left: 0; right: 0;
    top: 324px;
    text-align: center;
    font-size: 18px;
    color: var(--ink);
  }
  .cta-band {
    position: absolute;
    left: 0; right: 0;
    top: 362px;
    height: 29px;
    background: var(--brand-blue);
    color: var(--paper);
    text-align: center;
    font-size: 18px;
    line-height: 29px;
  }
</style>
</head>
<body>
  <section class="card card--front">
    <svg class="accent-panel" width="722" height="413" viewBox="0 0 722 413" aria-hidden="true">
      <path d="M508,0 C470,120 380,200 390,300 C398,380 460,413 540,413 L722,413 L722,0 Z" fill="#0f73bb"/>
      <path d="M508,0 C470,120 380,200 390,300 C398,380 460,413 540,413" fill="none" stroke="#e8202b" stroke-width="12"/>
    </svg>

    <div class="wordmark"><span class="wordmark__dot"></span>Brintell's</div>

    <div class="contact">
      <p class="contact__name">Dane Brintell</p>
      <p class="contact__line">
        <svg class="contact__icon" viewBox="0 0 24 24" aria-hidden="true"><path fill="#0f73bb" d="M6.6 10.8a15.1 15.1 0 0 0 6.6 6.6l2.2-2.2a1 1 0 0 1 1-.25 11.4 11.4 0 0 0 3.6.57 1 1 0 0 1 1 1V20a1 1 0 0 1-1 1A17 17 0 0 1 3 4a1 1 0 0 1 1-1h3.5a1 1 0 0 1 1 1c0 1.25.2 2.45.57 3.57a1 1 0 0 1-.25 1z"/></svg>
        555.014.2280
      </p>
      <p class="contact__line">
        <svg class="contact__icon" viewBox="0 0 24 24" aria-hidden="true"><rect x="2" y="5" width="20" height="15" rx="2" fill="#0f73bb"/><path d="M3 7l9 6 9-6" fill="none" stroke="#fff" stroke-width="2"/></svg>
        hvacbrintell@example.com
      </p>
    </div>

    <div class="credentials">
      <p>LICENSED &amp; INSURED</p>
      <p>FAMILY OWNED &amp; OPERATED</p>
    </div>
  </section>

  <section class="card card--back">
    <div class="wordmark"><span class="wordmark__dot"></span>Brintell's</div>
    <p class="service-area">Serves Millbrook, IA &amp; Surrounding Areas</p>
    <p class="cta-band">CALL TODAY FOR ALL YOUR HVAC, REFRIGERATION &amp; PLUMBING NEEDS</p>
  </section>
</body>
</html>
```